Education provider needs a landing page for its brand

We need a landing page for an advertising campaign that we are currently running on hireloop.com.au.
We're Tallowby Institute. We offer Australian online qualifications (courses) that help people get jobs with the right knowledge.
We'd like a landing page that shows our quirky, fun style that breaks away from traditional, conservative education advertising. The final landing page needs to be a strong converter for leads as it can take up to 90 days for someone to decide to study a course.
Check out our website. www.tallowby.edu.au

We also like the attached landing pages by Zivo and Pell Academy.

Target Market(s)

25-45 yr olds who have recently searched for a course to study on Hireloop.

Font styles to use
Sans Serif

Colors
3276b5
85acd3
ecf5f6
87d0c7

Requirements
Must have
• - Simple and uncluttered
- Logo
- Video - https://vidhost.example/v/Qw8mXz2LkTa
- 3 x dot points about why Tallowby is your best educator partner
- It needs a lead form to capture user's details so we can nurture them in an email campaign. This will be a 'Learn More' button that allows them to add their name and email address and they will be sent information.
- 'Enrol Now' button
Nice to have
• - Simple list of courses that we offer

```html
<!DOCTYPE html>
<html lang="en">
<head>
<meta charset="utf-8">
<title>Tallowby Institute – Why Tallowby</title>
<link href="https://fonts.googleapis.com/css2?family=Montserrat:wght@500;600&family=Roboto:wght@400&display=swap" rel="stylesheet">
<style>
:root{
  --navy:#1f3350;
  --blue:#3276b5;
  --teal:#87d0c7;
  --ink:#1a1a1a;
  --text:#555;
  --line:#d9d9d9;
  --footer:#333333;
}
*{box-sizing:border-box;margin:0;padding:0}
html,body{width:1200px;height:2591px;overflow:hidden;background:#fff;font-family:Roboto,Arial,sans-serif;color:var(--text)}
.page{position:relative;width:1200px;height:2591px}
.brand{position:absolute;left:89px;top:0;width:97px;height:97px;background:var(--navy);display:flex;flex-direction:column;align-items:center;justify-content:center;color:#fff;font-family:Montserrat,sans-serif;font-weight:500;text-align:center}
.brand .sq{width:26px;height:26px;background:#fff;margin-bottom:10px}
.brand .name{font-size:12px;letter-spacing:.5px;line-height:1.2}
.brand .sub{font-size:7px;letter-spacing:1px}
.nav{position:absolute;top:38px;left:0;font-size:15px;color:#444}
.nav a{position:absolute;white-space:nowrap;color:#444;text-decoration:none}
.nav a.active{color:var(--teal)}
.phone{position:absolute;left:947px;top:34px;color:var(--blue);font-size:23px;display:flex;align-items:center;gap:8px}
.why{position:absolute;left:89px;top:124px}
.why h1{font-family:Montserrat,sans-serif;font-weight:600;font-size:34px;color:var(--ink);margin-bottom:12px}
.why ul{list-style:none;font-size:14.5px;line-height:27px;color:#555}
.why li{position:relative;padding-left:27px;width:500px}
.why li::before{content:"»";position:absolute;left:0;color:var(--blue)}
.btn{display:inline-flex;align-items:center;justify-content:center;background:var(--teal);color:#fff;font-size:16px;border:0}
.learn{position:absolute;left:89px;top:290px;width:164px;height:41px}
.video{position:absolute;left:0;top:360px;width:1200px;height:600px;
  background:
    radial-gradient(ellipse 160px 120px at 300px 120px,rgba(255,236,200,.55),transparent 70%),
    radial-gradient(ellipse 220px 160px at 600px 250px,rgba(224,170,120,.55),transparent 70%),
    radial-gradient(ellipse 380px 140px at 520px 470px,rgba(170,110,110,.55),transparent 70%),
    radial-gradient(ellipse 300px 120px at 900px 500px,rgba(150,120,110,.45),transparent 70%),
    radial-gradient(ellipse 200px 200px at 80px 260px,rgba(130,120,90,.5),transparent 70%),
    linear-gradient(180deg,#5c4838 0%,#4a3829 45%,#3a2c22 100%)}
.play{position:absolute;left:560px;top:620px}
.quote{position:absolute;left:733px;top:129px;width:377px;height:440px;background:#fff;box-shadow:0 0 12px rgba(0,0,0,.12);padding:26px 26px 0}
.quote h2{font-family:Montserrat,sans-serif;font-weight:500;font-size:32px;color:var(--ink);text-align:center;margin-bottom:10px}
.field{display:block;width:325px;height:38px;border:1px solid var(--line);margin-bottom:7px;font-size:15px;padding:10px 16px;color:#666}
.field.msg{height:110px}
.enrol{width:325px;height:38px;margin-top:1px}
.courses-title{position:absolute;top:1048px;left:0;width:1200px;text-align:center;font-family:Montserrat,sans-serif;font-weight:500;font-size:42px;color:var(--ink)}
.card{position:absolute;width:331px;height:371px;overflow:hidden}
.card::after{content:"";position:absolute;left:0;right:0;bottom:0;height:140px;background:linear-gradient(180deg,transparent,rgba(0,0,0,.35))}
.card .tag{position:absolute;left:0;bottom:0;width:91px;height:82px;background:var(--teal);border-top-right-radius:82px 82px;z-index:1}
.card .tag svg{position:absolute;left:12px;top:22px}
.card .label{position:absolute;left:102px;bottom:24px;color:#fff;font-family:Montserrat,sans-serif;font-weight:600;font-size:19px;line-height:25px;z-index:1;white-space:nowrap}
.footer{position:absolute;left:0;top:2352px;width:1200px;height:239px;background:var(--footer);color:#fff}
.footer .brand{left:563px;top:55px;width:75px;height:75px}
.footer .brand .sq{width:20px;height:20px;margin-bottom:6px}
.footer .brand .name{font-size:9px}
.footer .brand .sub{font-size:5px}
.flinks a{position:absolute;top:157px;font-size:16px;color:#fff;text-decoration:none}
.copy{position:absolute;top:195px;left:0;width:1200px;text-align:center;font-size:12px}
</style>
</head>
<body>
<div class="page">
  <div class="brand"><span class="sq"></span><span class="name">TALLOWBY</span><span class="sub">INSTITUTE</span></div>
  <nav class="nav">
    <a class="active" style="left:311px">Courses</a>
    <a style="left:409px">About</a>
    <a style="left:494px">More info</a>
    <a style="left:596px">Contact</a>
    <a style="left:692px">Blog</a>
    <a style="left:759px">Student Login</a>
  </nav>
  <div class="phone"><svg width="18" height="18" viewBox="0 0 24 24"><path fill="#3276b5" d="M6.6 10.8a15.1 15.1 0 0 0 6.6 6.6l2.2-2.2c.3-.3.7-.4 1-.2 1.1.4 2.3.6 3.6.6.6 0 1 .4 1 1V20c0 .6-.4 1-1 1C10.6 21 3 13.4 3 4c0-.6.4-1 1-1h3.5c.6 0 1 .4 1 1 0 1.3.2 2.5.6 3.6.1.3 0 .7-.2 1z"/></svg>1300 555 014</div>

  <section class="why">
    <h1>Why Tallowby</h1>
    <ul>
      <li>Learn skills that are relevant</li>
      <li>Australia's highest-rated private training institute</li>
      <li>Last year Tallowby Institute trained more tax agents and bookkeepers than any other private institute</li>
    </ul>
  </section>
  <a class="btn learn">Learn More</a>

  <div class="video" role="img" aria-label="Video still: two girls watching a tablet in a cosy bedroom with fairy lights"></div>
  <svg class="play" width="80" height="80" viewBox="0 0 80 80"><circle cx="40" cy="40" r="39" fill="#1d2b2a" opacity=".6"/><circle cx="40" cy="40" r="31" fill="#87d0c7"/><path d="M36 33l10 7-10 7z" fill="#fff"/></svg>

  <form class="quote">
    <h2>Get A Quote</h2>
    <div class="field">First Name</div>
    <div class="field">Last Name</div>
    <div class="field">Email</div>
    <div class="field">Phone No</div>
    <div class="field msg">Message</div>
    <div class="btn enrol">Enrol Now</div>
  </form>

  <h2 class="courses-title">Courses We Offered</h2>

  <div class="card" style="left:89px;top:1116px;background:radial-gradient(ellipse 140px 110px at 230px 170px,rgba(40,40,50,.45),transparent 70%),radial-gradient(ellipse 160px 120px at 120px 120px,rgba(240,200,180,.7),transparent 70%),linear-gradient(160deg,#eef3f7 0%,#d6dfe6 50%,#b7c4cf 100%)" role="img" aria-label="Photo: hands using a calculator over financial papers"><div class="tag"><svg width="54" height="50" fill="none" stroke="#fff" stroke-width="2"><rect x="2" y="8" width="36" height="40"/><rect x="30" y="2" width="20" height="30"/></svg></div><div class="label">Accounting</div></div>
  <div class="card" style="left:434px;top:1116px;background:radial-gradient(ellipse 120px 80px at 170px 180px,rgba(110,140,170,.6),transparent 70%),radial-gradient(ellipse 160px 120px at 240px 90px,rgba(230,200,180,.6),transparent 70%),linear-gradient(160deg,#6c7486 0%,#d9d6d2 45%,#8d8f94 100%)" role="img" aria-label="Photo: people pointing at charts on a tablet"><div class="tag"><svg width="54" height="50" fill="none" stroke="#fff" stroke-width="2"><rect x="4" y="6" width="34" height="40"/><rect x="30" y="22" width="18" height="24"/></svg></div><div class="label">Financial Planning</div></div>
  <div class="card" style="left:779px;top:1116px;background:radial-gradient(ellipse 110px 160px at 80px 220px,rgba(160,200,220,.7),transparent 70%),radial-gradient(ellipse 110px 180px at 260px 240px,rgba(30,60,70,.8),transparent 70%),linear-gradient(160deg,#d7dadb 0%,#a8b4b8 50%,#556b70 100%)" role="img" aria-label="Photo: smiling colleagues in an office"><div class="tag"><svg width="54" height="50" fill="none" stroke="#fff" stroke-width="2"><circle cx="20" cy="30" r="12"/><circle cx="40" cy="12" r="6"/></svg></div><div class="label">Business Management</div></div>

  <div class="card" style="left:89px;top:1501px;background:radial-gradient(ellipse 90px 140px at 80px 220px,rgba(220,220,60,.6),transparent 70%),radial-gradient(ellipse 80px 120px at 260px 220px,rgba(210,210,80,.5),transparent 70%),radial-gradient(ellipse 160px 90px at 230px 320px,rgba(170,140,100,.8),transparent 70%),linear-gradient(160deg,#2d4a84 0%,#4f6a9a 45%,#8d8878 100%)" role="img" aria-label="Photo: warehouse workers in hard hats"><div class="tag"><svg width="54" height="50" fill="none" stroke="#fff" stroke-width="2"><rect x="2" y="14" width="32" height="22"/><rect x="34" y="22" width="14" height="14"/><circle cx="12" cy="42" r="4"/><circle cx="40" cy="42" r="4"/></svg></div><div class="label">Logistics</div></div>
  <div class="card" style="left:434px;top:1501px;background:radial-gradient(ellipse 150px 120px at 170px 270px,rgba(60,100,160,.85),transparent 70%),radial-gradient(ellipse 90px 90px at 170px 90px,rgba(180,120,90,.6),transparent 70%),linear-gradient(160deg,#e7e0d4 0%,#d2cbc0 45%,#9aa7b8 100%)" role="img" aria-label="Photo: man in glasses reading a document"><div class="tag"><svg width="54" height="50" fill="none" stroke="#fff" stroke-width="2"><circle cx="16" cy="14" r="9"/><circle cx="34" cy="14" r="9"/><path d="M4 44h20l10-10"/></svg></div><div class="label">Finance and<br>Mortgage broking</div></div>
  <div class="card" style="left:779px;top:1501px;background:radial-gradient(ellipse 120px 80px at 150px 140px,rgba(230,225,215,.6),transparent 70%),radial-gradient(ellipse 120px 80px at 90px 60px,rgba(210,210,220,.6),transparent 70%),radial-gradient(ellipse 140px 80px at 200px 320px,rgba(60,70,90,.6),transparent 70%),linear-gradient(160deg,#9a7a5c 0%,#8a6a4e 50%,#6e5846 100%)" role="img" aria-label="Photo: team working around a wooden table"><div class="tag"><svg width="54" height="50" fill="none" stroke="#fff" stroke-width="2"><rect x="4" y="8" width="30" height="38"/><path d="M44 6v36"/></svg></div><div class="label">Project Management</div></div>

  <div class="card" style="left:89px;top:1886px;background:radial-gradient(ellipse 120px 50px at 140px 265px,rgba(255,220,170,.8),transparent 70%),radial-gradient(ellipse 150px 90px at 170px 170px,rgba(240,120,50,.45),transparent 70%),radial-gradient(ellipse 120px 60px at 150px 80px,rgba(200,140,110,.4),transparent 70%),linear-gradient(160deg,#0d0d0d 0%,#1a1614 60%,#2a1e16 100%)" role="img" aria-label="Photo: hands over a phone with glowing app symbols"><div class="tag"><svg width="54" height="50" fill="none" stroke="#fff" stroke-width="2"><circle cx="26" cy="26" r="18"/><circle cx="26" cy="26" r="8"/></svg></div><div class="label">Marketing</div></div>
  <div class="card" style="left:434px;top:1886px;background:radial-gradient(circle 100px at 170px 180px,rgba(180,190,220,.55),transparent 70%),radial-gradient(ellipse 90px 120px at 20px 120px,rgba(190,150,170,.55),transparent 70%),linear-gradient(160deg,#566a94 0%,#33446c 50%,#1d2b4c 100%)" role="img" aria-label="Photo: person touching a digital compliance checklist"><div class="tag"><svg width="54" height="50" fill="none" stroke="#fff" stroke-width="2"><rect x="4" y="20" width="20" height="26"/><rect x="30" y="4" width="18" height="40"/></svg></div><div class="label">Governance</div></div>
  <div class="card" style="left:779px;top:1886px;background:radial-gradient(ellipse 120px 110px at 220px 180px,rgba(70,90,150,.6),transparent 70%),radial-gradient(ellipse 140px 70px at 260px 310px,rgba(200,120,200,.45),transparent 70%),radial-gradient(ellipse 110px 110px at 70px 160px,rgba(30,30,30,.7),transparent 70%),linear-gradient(160deg,#5d5048 0%,#7a6e66 50%,#a9a39c 100%)" role="img" aria-label="Photo: student with headphones studying at a laptop"><div class="tag"><svg width="54" height="50" fill="none" stroke="#fff" stroke-width="2"><rect x="4" y="18" width="30" height="28"/><rect x="28" y="4" width="20" height="16"/></svg></div><div class="label">Short courses</div></div>

  <footer class="footer">
    <div class="brand"><span class="sq"></span><span class="name">TALLOWBY</span><span class="sub">INSTITUTE</span></div>
    <div class="flinks">
      <a style="left:326px">Courses</a>
      <a style="left:424px">About</a>
      <a style="left:510px">More info</a>
      <a style="left:611px">Contact</a>
      <a style="left:707px">Blog</a>
      <a style="left:774px">Student Login</a>
    </div>
    <div class="copy">© 2020The Company Name.All Rights Reserved.Privacy Policy</div>
  </footer>
</div>
</body>
</html>
```